Velto Business Card

1. We need a double sided business card ready to print by Wed 26 June.
2. Our business name is Velto
3. We trade under the name Velto Consult.
4. The card will be printed by Pib or CardNorra on a 85mmx55mm card with rounded edges (standard size). The card will be on a luxury finish and we dont mind the logo or contact details being embossed in silver or a suitable colour.
5. The card should be simple and classy representing a management consultancy. Slimmer and large fonts should be used
6. Our website is www.veltoconsult.example
7. We dont want a tag line
8. The cards are for three partners, therefore the same design will be used to add details for each of the 3 partners, therefore the files we receive should be editable.
9. The contact details to include as a minimum:
Name First Name Last Name
Position: Partner
Telephone +44 7612 555 123
email: first.last@veltoconsult.example
10. This is our linkedIn Page: https://www.linkedin.example/company/velto-group/ to get an idea of our business (do not use on the card)
11. We want one side to have the logo in the middle, could be silver and embossed with a single dark blue colour in the background.
12. Our accent (>) and contact details should be on the reverse side with a white background, perhaps replace the website with QR code.
13. The text should be legible and large and look classy and professional, maybe slimmer fonts
14. You do not need to keep to the colours we have provided, be creative
15. We want the original files, vectors, jpeg, .ai and .png files ready to print.
16. We want the options to make several revisions to get the card right.

```html
<!DOCTYPE html>
<html lang="en">
<head>
<meta charset="utf-8">
<title>Velto Business Card</title>
<link rel="stylesheet" href="https://fonts.googleapis.com/css2?family=Montserrat:wght@400;500;700;800&display=swap">
<style>
  :root {
    --page-bg: #e4e5e8;
    --card-white: #ffffff;
    --navy: #0e1235;
    --ink: #1a1a22;
    --amber-top: #ffc516;
    --amber-bottom: #f28a20;
    --card-shadow: 0 14px 30px rgba(20, 22, 40, 0.18);
  }
  * { box-sizing: border-box; margin: 0; padding: 0; }
  html, body { width: 1200px; height: 800px; overflow: hidden; }
  body {
    background: var(--page-bg);
    font-family: "Montserrat", sans-serif;
    position: relative;
  }
  .card {
    position: absolute;
    top: 232px;
    width: 520px;
    height: 336px;
    border-radius: 26px;
    box-shadow: var(--card-shadow);
    overflow: hidden;
  }
  .card--back {
    left: 50px;
    background: linear-gradient(180deg, var(--amber-top) 0%, var(--amber-bottom) 70%);
    display: flex;
    align-items: center;
    justify-content: center;
  }
  .back-name {
    font-weight: 800;
    font-size: 64px;
    letter-spacing: -1px;
    color: var(--amber-bottom);
    text-shadow: none;
    filter: brightness(0.96);
  }
  .card--front {
    left: 630px;
    background: var(--card-white);
  }
  .wordmark {
    position: absolute;
    left: 200px;
    top: 28px;
    font-weight: 800;
    font-size: 92px;
    line-height: 1;
    letter-spacing: -3px;
    color: var(--navy);
  }
  .details {
    position: absolute;
    left: 214px;
    top: 136px;
    color: var(--ink);
  }
  .person-name {
    font-weight: 800;
    font-size: 22px;
    color: var(--navy);
    letter-spacing: 0.2px;
  }
  .person-role {
    font-weight: 400;
    font-size: 13px;
    margin-top: 2px;
  }
  .address {
    font-size: 12.5px;
    line-height: 1.35;
    margin-top: 20px;
  }
  .contact-list {
    list-style: none;
    margin-top: 16px;
  }
  .contact-list li {
    display: flex;
    align-items: center;
    gap: 10px;
    font-size: 12.5px;
    line-height: 1.9;
  }
  .contact-list svg { width: 13px; height: 13px; fill: var(--navy); flex: none; }
</style>
</head>
<body>

  <section class="card card--back" aria-label="Card back">
    <span class="back-name">Velto</span>
  </section>

  <section class="card card--front" aria-label="Card front">
    <div class="wordmark">velto</div>

    <div class="details">
      <p class="person-name">Daniel Hart</p>
      <p class="person-role">Partner</p>

      <p class="address">418 Harbor Row,<br>Easton, Maine 04740</p>

      <ul class="contact-list">
        <li>
          <svg viewBox="0 0 16 16" aria-hidden="true"><path d="M2 5c0-2 2-3 6-3s6 1 6 3v1h-3V4.8C10 4.3 9 4 8 4s-2 .3-3 .8V6H2zM4 7h8l2 5v2H2v-2zm4 1.5a2 2 0 1 0 0 4 2 2 0 0 0 0-4z"/></svg>
          <span>+44 7612 555 123</span>
        </li>
        <li>
          <svg viewBox="0 0 16 16" aria-hidden="true"><path d="M1 3h14v10H1zm1.5 1.2v.3L8 8.6l5.5-4.1v-.3z"/></svg>
          <span>first.last@veltoconsult.example</span>
        </li>
        <li>
          <svg viewBox="0 0 16 16" aria-hidden="true"><path d="M8 1a7 7 0 1 0 0 14A7 7 0 0 0 8 1zm0 1.5c.9 0 2 1.8 2.3 4.5H5.7C6 4.3 7.1 2.5 8 2.5zM5.7 9h4.6c-.3 2.7-1.4 4.5-2.3 4.5S6 11.7 5.7 9z"/></svg>
          <span>www.veltoconsult.example</span>
        </li>
      </ul>
    </div>
  </section>

</body>
</html>
```